Corporate Design zur Markenbildung im Bereich Notfallsimulation und - Training
Zielgruppe
Trainieren und Simulieren von medizinischen Notfällen in Arztpraxen, Krankenhäusern, Pflegeheimen und großen Firmen
Aufgabenstellung
Der Geschäftszweig soll als eigene innovative Marke entwickelt werden. Das Logo soll klare und einfache Formen und Strukturen aufweisen. Der Name VitoPlex muss im Logo enthalten sein. Ein Bezug zu Notfallmedizin muss klar erkennbar sein. Die Grundbestandteile für die Wortwahl liegen in Rettung, Qualität und Training.

```html
<!DOCTYPE html>
<html lang="de">
<head>
<meta charset="utf-8">
<title>VitoPlex Briefbogen</title>
<link rel="stylesheet" href="https://fonts.googleapis.com/css2?family=Questrial&display=swap">
<style>
  :root {
    --ink: #333333;
    --ink-soft: #444444;
    --rule: #555555;
    --frame: #9a9a9a;
    --paper: #ffffff;
  }
  html, body { margin: 0; padding: 0; overflow: hidden; background: var(--paper); }
  .letterhead {
    position: relative;
    width: 850px; height: 1200px;
    box-sizing: border-box;
    border: 1px solid var(--frame);
    background: var(--paper);
    font-family: "Questrial", "Century Gothic", sans-serif;
    color: var(--ink);
    overflow: hidden;
  }
  .brand {
    position: absolute; left: 500px; top: 76px;
    display: flex; align-items: center; gap: 12px;
    font-size: 50px; line-height: 1; color: var(--ink);
  }
  .brand-dot { width: 14px; height: 14px; border-radius: 50%; background: var(--ink); }
  .sender-line {
    position: absolute; left: 50px; top: 201px;
    font-size: 14px; color: var(--ink-soft); white-space: nowrap;
  }
  .contact-name {
    position: absolute; left: 580px; top: 195px;
    font-size: 20px; color: var(--ink); letter-spacing: 0.3px; white-space: nowrap;
  }
  .contact-block {
    position: absolute; left: 580px; top: 242px; height: 158px;
    border-left: 2px solid var(--rule); padding-left: 9px;
    font-style: normal; font-size: 17.5px; line-height: 21.2px;
    color: var(--ink-soft); white-space: nowrap;
  }
  .contact-block p { margin: 0; }
  .contact-block p:first-child { margin-top: 5px; }
  .parent-brand {
    position: absolute; left: 41px; top: 1056px;
    display: flex; align-items: flex-end; gap: 10px; white-space: nowrap;
  }
  .parent-label { font-size: 13px; color: var(--ink-soft); padding-bottom: 2px; }
  .parent-name { font-size: 19px; line-height: 1; color: var(--ink); }
  .bank-row {
    position: absolute; left: 0; top: 1102px; width: 100%; height: 66px;
    font-size: 12px; color: var(--ink-soft); white-space: nowrap;
  }
  .bank-row span { position: absolute; top: 0; height: 66px; padding-top: 25px; box-sizing: border-box; }
  .bank-row .divided { border-left: 1px solid var(--rule); padding-left: 10px; }
  .bank-row .bank { left: 41px; }
  .bank-row .iban { left: 173px; }
  .bank-row .bic { left: 378px; }
  .bank-row .tax { left: 514px; }
  .bank-row .vat { left: 670px; }
</style>
</head>
<body>
<main class="letterhead">
  <header class="brand">
    <span>VitoPlex</span><span class="brand-dot"></span>
  </header>

  <div class="sender-line">VitoPlex Lindenweg 12 D-53919 Weilerbach</div>

  <div class="contact-name">Jonas B. Brettler</div>
  <address class="contact-block">
    <p>Lindenweg 12</p>
    <p>D-53919 Weilerbach</p>
    <p>Tel: +49 2455 6204917</p>
    <p>Mobil: +49 15730681246</p>
    <p>Fax: +49 2455 708241</p>
    <p>info@VitoPlex.de</p>
    <p>www.VitoPlex.de</p>
  </address>

  <footer>
    <div class="parent-brand">
      <span class="parent-label">Eine Marke von</span>
      <span class="parent-name">Werkraum Nord</span>
    </div>
    <div class="bank-row">
      <span class="bank">Nordring Bank AG</span>
      <span class="iban divided">IBAN DE47 300512840736192500</span>
      <span class="bic divided">BIC NORBDEHH214</span>
      <span class="tax divided">Steuernr. 214/6093/1528</span>
      <span class="vat divided">USt-IdNr. DE309471562</span>
    </div>
  </footer>
</main>
</body>
</html>
```